Business Card / Appointment Card for Physician

On one side it should give the logo, address, and contact information, and on the other side it should br an Appointment card.

One Side:
Logo (see attached files)
Board Certified American Orthopedic Surgery

1487 Harrowgate Ave.
Suite KM7
Bronx, NY 10527
Tel: (718) 552 - 1948
Fax: (718) 552 - 7210

628 Fourth Ave.
Suite 42
New York, NY 10087
Tel: (212) 734 - 2815

Second Side:
Appointment
give them a choice of Bronx or Mahattan office
For:
Date:
Time:

If you are unable to keep your appointment, please call (718) 263-5102 24hrs in advance.

Target Market(s)

People that need orthopedic surgery

Industry/Entity Type

Business

Contact Information for Business Card

smart and attractive

Requirements
Must have
• logo
• contact information on one side, appointment information on the other

```html
<!DOCTYPE html>
<html lang="en">
<head>
<meta charset="utf-8">
<title>Daniel R. Whitford MD PC – Business &amp; Appointment Card</title>
<link href="https://fonts.googleapis.com/css2?family=Roboto:wght@400;500;700&family=Roboto+Condensed:wght@400&family=Open+Sans:wght@300;700&display=swap" rel="stylesheet">
<style>
  :root {
    --page-bg: #d4d4d4;
    --card-white: #ffffff;
    --brand-blue: #3f628b;
    --brand-dark: #2b4262;
    --fold-dark: #2a3d5c;
    --name-blue: #3a5f8e;
    --text-grey: #4a4a4a;
    --label-grey: #555555;
    --rule-grey: #9a9a9a;
  }
  * { box-sizing: border-box; margin: 0; padding: 0; }
  html, body { width: 1200px; height: 1200px; overflow: hidden; background: var(--page-bg); }
  .canvas { position: relative; width: 1200px; height: 1200px; }

  .card { position: absolute; left: 192px; width: 814px; height: 452px; }
  .card-front { top: 86px; background: var(--card-white); box-shadow: 0 26px 30px -14px rgba(0,0,0,.45); }
  .card-back { top: 596px; background: var(--brand-blue); box-shadow: 0 26px 30px -14px rgba(0,0,0,.45); }

  /* front */
  .brand-mark { position: absolute; left: 357px; top: 26px; width: 100px; height: 100px; border-radius: 50%; background: var(--brand-blue); }
  .brand-name { position: absolute; left: 0; right: 0; top: 138px; text-align: center; font-family: "Roboto", sans-serif; font-weight: 400; font-size: 37px; letter-spacing: -0.5px; color: var(--name-blue); line-height: 1; }
  .brand-tagline { position: absolute; left: 0; right: 0; top: 180px; text-align: center; font-family: "Roboto", sans-serif; font-weight: 400; font-size: 19px; color: var(--name-blue); line-height: 1; }
  .cert-band { position: absolute; left: 0; right: 0; top: 212px; height: 59px; background: var(--brand-blue); color: #fff; font-family: "Roboto", sans-serif; font-weight: 500; font-size: 29px; display: flex; align-items: center; justify-content: center; }
  .band-fold { position: absolute; top: 271px; width: 24px; height: 24px; }
  .band-fold-left { left: 0; }
  .band-fold-right { right: 0; }
  .office { position: absolute; left: 0; right: 0; text-align: center; font-family: "Roboto Condensed", sans-serif; font-size: 27px; color: var(--text-grey); line-height: 31px; }
  .office-bronx { top: 278px; }
  .office-manhattan { top: 358px; }
  .office-rule { position: absolute; left: 118px; width: 580px; top: 350px; height: 1px; background: var(--rule-grey); }
  .front-base { position: absolute; left: 0; right: 0; bottom: 0; height: 18px; background: var(--fold-dark); }

  /* back */
  .tab-fold { position: absolute; top: 0; width: 18px; height: 18px; }
  .tab-fold-left { left: 197px; }
  .tab-fold-right { left: 597px; }
  .title-tab { position: absolute; left: 215px; top: 0; width: 382px; height: 66px; background: var(--card-white); border-radius: 0 0 14px 14px; display: flex; align-items: center; justify-content: center; font-family: "Roboto", sans-serif; font-weight: 700; font-size: 42px; letter-spacing: 4px; color: var(--name-blue); }
  .office-choice { position: absolute; left: 54px; top: 97px; display: flex; align-items: center; font-family: "Roboto", sans-serif; font-weight: 500; font-size: 28px; color: #fff; }
  .checkbox { width: 28px; height: 28px; background: var(--card-white); margin-right: 9px; }
  .choice-label { margin-right: 14px; }
  .field { position: absolute; background: var(--card-white); font-family: "Roboto", sans-serif; font-weight: 500; font-size: 27px; color: var(--label-grey); padding: 6px 13px; }
  .field-for { left: 54px; top: 137px; width: 706px; height: 150px; }
  .field-date { left: 54px; top: 296px; width: 347px; height: 53px; padding-top: 10px; }
  .field-time { left: 413px; top: 296px; width: 347px; height: 53px; padding-top: 10px; }
  .cancel-note { position: absolute; left: 0; right: 0; top: 360px; text-align: center; font-family: "Open Sans", sans-serif; font-weight: 300; font-size: 28px; line-height: 31px; color: #fff; }
  .cancel-note strong { font-weight: 700; }
</style>
</head>
<body>
<div class="canvas">

  <section class="card card-front">
    <div class="brand-mark"></div>
    <div class="brand-name">DANIEL R. WHITFORD MD PC</div>
    <div class="brand-tagline">ORTHOPAEDIC SURGERY &amp; SPORTS MEDICINE</div>
    <div class="cert-band">Board Certified American Orthopedic Surgery</div>
    <svg class="band-fold band-fold-left" viewBox="0 0 24 24"><polygon points="0,0 24,0 0,24" fill="var(--fold-dark)"/></svg>
    <svg class="band-fold band-fold-right" viewBox="0 0 24 24"><polygon points="0,0 24,0 24,24" fill="var(--fold-dark)"/></svg>
    <div class="office office-bronx">
      <p>1487 Harrowgate Ave. Suite KM7, Bronx, NY 10527</p>
      <p>Tel: (718) 552 - 1948 &nbsp;|&nbsp; Fax: (718) 552 - 7210</p>
    </div>
    <div class="office-rule"></div>
    <div class="office office-manhattan">
      <p>628 Fourth Ave. Suite 42, New York, NY 10087</p>
      <p>Tel: (212) 734 - 2815</p>
    </div>
    <div class="front-base"></div>
  </section>

  <section class="card card-back">
    <svg class="tab-fold tab-fold-left" viewBox="0 0 18 18"><polygon points="0,0 18,0 18,18" fill="var(--fold-dark)"/></svg>
    <svg class="tab-fold tab-fold-right" viewBox="0 0 18 18"><polygon points="0,0 18,0 0,18" fill="var(--fold-dark)"/></svg>
    <div class="title-tab">APPOINTMENT</div>
    <div class="office-choice">
      <span class="checkbox"></span><span class="choice-label">Bronx</span>
      <span class="checkbox"></span><span class="choice-label">Mahattan</span>
    </div>
    <div class="field field-for">For:</div>
    <div class="field field-date">Date:</div>
    <div class="field field-time">Time:</div>
    <p class="cancel-note">If you are unable to keep your appointment,<br>Please call <strong>(718) 263-5102</strong> 24hrs in advance.</p>
  </section>

</div>
</body>
</html>
```